Image Ads needed for a Pharmacy Education e-commerce website

I need image ads with these specifications:

Supported formats: JPG, PNG, GIF
File size: 3MB max
Recommended aspect ratios: 1:1 square; 4:5 portrait; 4:3 landscape; 16:9 landscape
Recommended resolutions: 1080x1080 square, 1080x1350 portrait, 1440x1080 landscape, 1920x1080 landscape
Thumbnail: Displays at 400x300 pixels
Thumbnail file size: 500KB max

```html
<!DOCTYPE html>
<html lang="en">
<head>
<meta charset="utf-8">
<title>Tovriq Ad Set</title>
<link rel="stylesheet" href="https://fonts.googleapis.com/css2?family=Baloo+2:wght@500;600;700&family=Nunito:wght@300;400;600&family=Oswald:wght@600&display=swap">
<style>
  :root{
    --board:#f5f0f0;
    --navy:#2d2c52;
    --green:#5a9e34;
    --white:#ffffff;
    --paper:#f7f7f8;
    --ink:#2d2c52;
    --caption:#2b2b2b;
  }
  *{box-sizing:border-box;margin:0;padding:0}
  html,body{width:1200px;height:1038px;overflow:hidden;background:var(--board)}
  body{position:relative;font-family:"Nunito",sans-serif;color:var(--ink)}
  .ad{position:absolute;overflow:hidden;box-shadow:0 1px 3px rgba(0,0,0,.06)}
  .abs{position:absolute}
  .brand{font-family:"Baloo 2",sans-serif;font-weight:700;color:var(--navy);line-height:1;white-space:nowrap}
  .brand.light{color:var(--white)}
  .display{font-family:"Baloo 2",sans-serif;font-weight:700;line-height:1}
  .caption{position:absolute;font-family:"Nunito",sans-serif;font-weight:400;font-size:13px;color:var(--caption);text-align:center;transform:translateX(-50%);white-space:nowrap}
  .contact{position:absolute;display:flex;align-items:center;gap:7px;font-family:"Nunito",sans-serif;font-weight:300;white-space:nowrap}
  .dot{display:inline-flex;align-items:center;justify-content:center;border-radius:50%;flex:none}
  .dot svg{display:block}

  /* 1920 x 1080 */
  .ad-wide{left:54px;top:76px;width:631px;height:355px;background:linear-gradient(135deg,#ffffff 0%,#f3f3f5 45%,#fbfbfc 100%)}
  .ad-wide .headline-band{left:0;top:131px;width:283px;height:108px;background:var(--navy);border-right:3px solid var(--green);border-bottom:3px solid var(--green);border-radius:0 6px 6px 0;padding:16px 0 0 35px;color:var(--white);font-size:33px}
  .ad-wide .price{left:517px;top:40px;width:114px;height:37px;background:var(--green);border-radius:12px 0 0 12px;color:var(--white);font-size:20px;display:flex;align-items:center;justify-content:center;padding-top:3px}
  .ad-wide .contact{font-size:10px;color:var(--navy)}

  /* 1080 x 1080 */
  .ad-square{left:781px;top:76px;width:355px;height:355px;background:var(--navy)}
  .ad-square .offer-band{left:0;top:275px;width:100%;height:34px;background:var(--green);color:var(--white);font-size:20px;display:flex;align-items:center;justify-content:center;padding-top:3px}
  .ad-square .contact{font-size:10px;color:var(--white)}

  /* 1080 x 1350 */
  .ad-portrait{left:54px;top:517px;width:355px;height:443px;background:var(--white)}
  .ad-portrait .price{left:243px;top:75px;width:112px;height:37px;background:var(--navy);border-radius:14px 0 0 14px;color:var(--white);font-size:20px;display:flex;align-items:center;justify-content:center;padding-top:3px}
  .ad-portrait .headline{left:0;top:340px;width:100%;text-align:center;font-family:"Oswald",sans-serif;font-weight:600;font-size:34px;color:var(--navy);letter-spacing:-.5px;transform:scaleX(.88)}
  .ad-portrait .footer{left:0;top:404px;width:100%;height:33px;background:var(--navy)}
  .ad-portrait .contact{font-size:10px;color:var(--white)}

  /* 1440 x 1080 */
  .ad-landscape{left:472px;top:517px;width:473px;height:354px;background:linear-gradient(110deg,#ffffff 0%,#ffffff 60%,#f2f2f4 60%,#f2f2f4 100%)}
  .ad-landscape .headline{left:44px;top:90px;font-size:42px;line-height:50px;color:var(--navy)}
  .ad-landscape .price{left:0;top:257px;width:137px;height:38px;background:var(--green);border-radius:0 14px 14px 0;color:var(--white);font-size:20px;display:flex;align-items:center;justify-content:center;padding-top:3px}
  .ad-landscape .contact{font-size:12px;color:var(--navy)}

  /* 400 x 300 thumbnail */
  .ad-thumb{left:1005px;top:517px;width:131px;height:98px;background:var(--paper);border-top:3px solid var(--green);border-bottom:3px solid var(--navy)}
  .ad-thumb .headline{left:0;top:40px;width:100%;text-align:center;font-size:11px;line-height:12px;color:var(--navy);font-weight:600}
  .ad-thumb .price{left:39px;top:72px;width:52px;height:14px;background:var(--green);border-radius:4px;color:var(--white);font-size:7px;display:flex;align-items:center;justify-content:center;font-family:"Baloo 2",sans-serif;font-weight:700;padding-top:1px}
</style>
</head>
<body>

<!-- 1920 x 1080 -->
<section class="ad ad-wide">
  <svg class="abs" style="left:0;top:0" width="631" height="355" aria-hidden="true">
    <path d="M256 355 C 275 250, 350 195, 430 215 C 500 232, 520 175, 570 160 C 605 150, 625 160, 631 170 L631 355 Z" fill="#2d2c52"/>
  </svg>
  <div class="abs" role="img" aria-label="Illustration of two pharmacists with a prescription, pill bottle and capsules" style="left:355px;top:92px;width:235px;height:255px;border-radius:40px;background:linear-gradient(160deg,rgba(223,234,246,.9),rgba(169,198,230,.55) 60%,rgba(214,40,90,.35))"></div>
  <div class="abs brand" style="left:36px;top:40px;font-size:38px">Tovriq</div>
  <div class="abs price display">$39 ONLY</div>
  <div class="abs headline-band display">Unlimited<br>QLCE Ceus</div>
  <div class="contact" style="left:34px;top:292px">
    <span class="dot" style="width:17px;height:17px;background:var(--navy)"><svg width="9" height="7" viewBox="0 0 18 14"><rect x="1" y="1" width="16" height="12" rx="2" fill="#fff"/><path d="M2 2 L9 8 L16 2" stroke="#2d2c52" stroke-width="2" fill="none"/></svg></span>info.tovriq.com
  </div>
  <div class="contact" style="left:34px;top:311px">
    <span class="dot" style="width:17px;height:17px;background:var(--navy)"><svg width="9" height="9" viewBox="0 0 24 24"><path d="M6.6 10.8a15 15 0 0 0 6.6 6.6l2.2-2.2a1 1 0 0 1 1-.25 11.4 11.4 0 0 0 3.6.57 1 1 0 0 1 1 1V20a1 1 0 0 1-1 1A17 17 0 0 1 3 4a1 1 0 0 1 1-1h3.5a1 1 0 0 1 1 1c0 1.25.2 2.45.57 3.57a1 1 0 0 1-.25 1z" fill="#fff"/></svg></span>(1) 555 010 0199
  </div>
</section>
<div class="caption" style="left:370px;top:453px">Tovriq 1920px x 1080 px</div>

<!-- 1080 x 1080 -->
<section class="ad ad-square">
  <div class="abs brand light" style="left:0;width:100%;text-align:center;top:30px;font-size:28px">Tovriq</div>
  <div class="abs" role="img" aria-label="Line drawing of a pharmacist at a counter with shelves, a plant and a computer" style="left:53px;top:80px;width:250px;height:168px;border-radius:125px 125px 0 0;background:linear-gradient(180deg,#3a3966,#33325c)"></div>
  <div class="abs offer-band display">Unlimited QLCE Ceus $39</div>
  <div class="contact" style="left:22px;top:323px">
    <span class="dot" style="width:17px;height:17px;background:var(--white)"><svg width="9" height="9" viewBox="0 0 24 24"><path d="M6.6 10.8a15 15 0 0 0 6.6 6.6l2.2-2.2a1 1 0 0 1 1-.25 11.4 11.4 0 0 0 3.6.57 1 1 0 0 1 1 1V20a1 1 0 0 1-1 1A17 17 0 0 1 3 4a1 1 0 0 1 1-1h3.5a1 1 0 0 1 1 1c0 1.25.2 2.45.57 3.57a1 1 0 0 1-.25 1z" fill="#5a9e34"/></svg></span>(1) 555 010 0199
  </div>
  <div class="contact" style="right:30px;top:323px">
    <span class="dot" style="width:17px;height:17px;background:var(--white)"><svg width="9" height="7" viewBox="0 0 18 14"><rect x="1" y="1" width="16" height="12" rx="2" fill="#5a9e34"/><path d="M2 2 L9 8 L16 2" stroke="#fff" stroke-width="2" fill="none"/></svg></span>info.tovriq.com
  </div>
</section>
<div class="caption" style="left:958px;top:453px">Tovriq 1080px X 1080px</div>

<!-- 1080 x 1350 -->
<section class="ad ad-portrait">
  <svg class="abs" style="left:0;top:0" width="355" height="340" aria-hidden="true">
    <path d="M0 38 C 50 26, 90 50, 150 66 C 220 84, 300 55, 355 46 L355 270 C 330 250, 300 240, 270 245 L0 200 Z" fill="#5a9e34"/>
  </svg>
  <div class="abs" role="img" aria-label="Illustration of a scientist presenting on a large laptop screen beside a DNA model and a student at a desk" style="left:21px;top:131px;width:318px;height:180px;border-radius:120px 90px 60px 60px;background:linear-gradient(160deg,#e7f0fa,#c9ddf1 55%,#6aa6d8)"></div>
  <div class="abs brand" style="left:0;width:100%;text-align:center;top:14px;font-size:30px">Tovriq</div>
  <div class="abs price display">$39 ONLY</div>
  <div class="abs headline">UNLIMITED QLCE CEUS</div>
  <div class="abs footer"></div>
  <div class="contact" style="left:18px;top:412px">
    <span class="dot" style="width:17px;height:17px;background:var(--white)"><svg width="9" height="9" viewBox="0 0 24 24"><path d="M6.6 10.8a15 15 0 0 0 6.6 6.6l2.2-2.2a1 1 0 0 1 1-.25 11.4 11.4 0 0 0 3.6.57 1 1 0 0 1 1 1V20a1 1 0 0 1-1 1A17 17 0 0 1 3 4a1 1 0 0 1 1-1h3.5a1 1 0 0 1 1 1c0 1.25.2 2.45.57 3.57a1 1 0 0 1-.25 1z" fill="#5a9e34"/></svg></span>(1) 555 010 0199
  </div>
  <div class="contact" style="right:32px;top:412px">
    <span class="dot" style="width:17px;height:17px;background:var(--white)"><svg width="9" height="7" viewBox="0 0 18 14"><rect x="1" y="1" width="16" height="12" rx="2" fill="#5a9e34"/><path d="M2 2 L9 8 L16 2" stroke="#fff" stroke-width="2" fill="none"/></svg></span>info.tovriq.com
  </div>
</section>
<div class="caption" style="left:227px;top:972px">Tovriq 1080px x 1350 px</div>

<!-- 1440 x 1080 -->
<section class="ad ad-landscape">
  <div class="abs brand" style="left:355px;top:31px;font-size:26px">Tovriq</div>
  <div class="abs headline display">Unlimited<br>QLCE<br>Ceus</div>
  <div class="abs" role="img" aria-label="Illustration of three pharmacists in white coats standing together" style="left:251px;top:85px;width:218px;height:215px;border-radius:30px;background:linear-gradient(180deg,#eef3fa,#c8d9ef 60%,#3d6fb8)"></div>
  <div class="abs price display">$39 ONLY</div>
  <div class="contact" style="left:32px;top:324px">
    <span class="dot" style="width:22px;height:22px;background:var(--navy)"><svg width="11" height="11" viewBox="0 0 24 24"><path d="M6.6 10.8a15 15 0 0 0 6.6 6.6l2.2-2.2a1 1 0 0 1 1-.25 11.4 11.4 0 0 0 3.6.57 1 1 0 0 1 1 1V20a1 1 0 0 1-1 1A17 17 0 0 1 3 4a1 1 0 0 1 1-1h3.5a1 1 0 0 1 1 1c0 1.25.2 2.45.57 3.57a1 1 0 0 1-.25 1z" fill="#fff"/></svg></span>(1) 555 010 0199
  </div>
  <div class="contact" style="left:325px;top:324px">
    <span class="dot" style="width:22px;height:22px;background:var(--navy)"><svg width="11" height="9" viewBox="0 0 18 14"><rect x="1" y="1" width="16" height="12" rx="2" fill="#fff"/><path d="M2 2 L9 8 L16 2" stroke="#2d2c52" stroke-width="2" fill="none"/></svg></span>info.tovriq.com
  </div>
</section>
<div class="caption" style="left:708px;top:894px">Tovriq 1440px x 1080 px</div>

<!-- 400 x 300 thumbnail -->
<section class="ad ad-thumb">
  <svg class="abs" style="left:0;top:0" width="131" height="92" aria-hidden="true">
    <path d="M0 27 L131 29 L131 31 L0 31 Z" fill="#5a9e34"/>
    <path d="M88 76 L131 76 L131 79 L88 80 Z" fill="#5a9e34"/>
  </svg>
  <div class="abs brand" style="left:0;width:100%;text-align:center;top:10px;font-size:11px">Tovriq</div>
  <div class="abs headline display">Unlimited<br>QLCE Ceus</div>
  <div class="abs price">$39 ONLY</div>
</section>
<div class="caption" style="left:1072px;top:631px">Tovriq 400x300</div>

</body>
</html>
```